The Bright Socket Business cards

one side I would like my logo (uploaded) and the other side I want my details. I'm an electrician in sydney. The logo side I'm happy with just a white background and our logo in the middle.

Details for other side
24/7 Sydney Electrician
Marcus Hale
0431 758 216
marcus@thebrightsocket.com.au
thebrightsocket.com.au
icons for facebook, instagram, linked in

electrician

company info

```html
<!DOCTYPE html>
<html lang="en">
<head>
<meta charset="utf-8">
<title>The Bright Socket – Business Cards</title>
<link rel="stylesheet" href="https://fonts.googleapis.com/css2?family=Montserrat:wght@400;600;700;800&display=swap">
<style>
  :root {
    --page-bg: #3a3a3a;
    --card-bg: #ffffff;
    --brand-red: #e8392a;
    --ink: #1d1d1d;
    --muted: #333333;
  }
  * { box-sizing: border-box; margin: 0; padding: 0; }
  html, body {
    width: 1200px;
    height: 875px;
    overflow: hidden;
    background: var(--page-bg);
    font-family: "Montserrat", Arial, sans-serif;
  }
  .sheet {
    width: 1200px;
    height: 875px;
    display: flex;
    align-items: center;
    justify-content: center;
    gap: 32px;
  }
  .card {
    width: 560px;
    height: 320px;
    background: var(--card-bg);
    border-radius: 22px;
    position: relative;
    box-shadow: 0 10px 30px rgba(0,0,0,.35);
  }
  .card--front {
    display: flex;
    align-items: center;
    justify-content: center;
  }
  .wordmark {
    color: var(--brand-red);
    font-weight: 800;
    font-size: 44px;
    letter-spacing: 1px;
    text-transform: uppercase;
    line-height: 1;
  }
  .card--back {
    display: flex;
    align-items: center;
    padding: 0 30px 0 36px;
  }
  .card--back .wordmark {
    font-size: 24px;
    width: 190px;
    flex: none;
    margin-top: 60px;
  }
  .divider {
    width: 2px;
    height: 150px;
    flex: none;
    background: var(--brand-red);
    margin: -30px 18px 0 10px;
  }
  .details {
    display: flex;
    flex-direction: column;
    margin-top: -20px;
  }
  .person-name {
    color: var(--brand-red);
    font-weight: 700;
    font-size: 20px;
    line-height: 1.2;
  }
  .tagline {
    color: var(--ink);
    font-weight: 600;
    font-size: 11px;
    letter-spacing: .5px;
    text-transform: uppercase;
    margin: 3px 0 10px;
  }
  .contact-line {
    display: flex;
    align-items: center;
    gap: 7px;
    font-size: 12.5px;
    color: var(--muted);
    line-height: 1.8;
    white-space: nowrap;
  }
  .contact-line svg { width: 11px; height: 11px; flex: none; }
  .social {
    display: flex;
    gap: 8px;
    margin: 20px 0 0 64px;
  }
  .social-square {
    width: 16px;
    height: 16px;
    border-radius: 4px;
    background: var(--brand-red);
  }
</style>
</head>
<body>
  <main class="sheet">
    <section class="card card--front" aria-label="Business card front">
      <p class="wordmark">The Bright Socket</p>
    </section>

    <section class="card card--back" aria-label="Business card back">
      <p class="wordmark">The Bright Socket</p>
      <span class="divider"></span>
      <div class="details">
        <p class="person-name">Marcus Hale</p>
        <p class="tagline">24/7 Sydney Electrician</p>
        <p class="contact-line">
          <svg viewBox="0 0 24 24" aria-hidden="true"><path fill="#e8392a" d="M6.6 10.8a15 15 0 0 0 6.6 6.6l2.2-2.2c.3-.3.7-.4 1-.2 1.1.4 2.3.6 3.6.6.6 0 1 .4 1 1V20c0 .6-.4 1-1 1A17 17 0 0 1 3 4c0-.6.4-1 1-1h3.5c.6 0 1 .4 1 1 0 1.3.2 2.5.6 3.6.1.3 0 .7-.2 1z"/></svg>
          0431 758 216
        </p>
        <p class="contact-line">
          <svg viewBox="0 0 24 24" aria-hidden="true"><rect x="2" y="5" width="20" height="14" rx="2" fill="#e8392a"/><path d="M3 6l9 7 9-7" stroke="#fff" stroke-width="2" fill="none"/></svg>
          marcus@thebrightsocket.com.au
        </p>
        <p class="contact-line">
          <svg viewBox="0 0 24 24" aria-hidden="true"><circle cx="12" cy="12" r="10" fill="#e8392a"/><path d="M2 12h20M12 2c3 3 3 17 0 20M12 2c-3 3-3 17 0 20" stroke="#fff" stroke-width="1.6" fill="none"/></svg>
          thebrightsocket.com.au
        </p>
        <div class="social" aria-label="Social media">
          <span class="social-square"></span>
          <span class="social-square"></span>
          <span class="social-square"></span>
        </div>
      </div>
    </section>
  </main>
</body>
</html>
```